Review Site Redesign

We have a rather ambitious goal to reinvent (redesign) the way bank financial review sites present information. In that respect, we’re looking for an innovative creative design.
As examples of what I would call bad or boring design please look at the following sites:
1. http://brisklend.example/se
2. http://vantorquay.example/se/privatlan
3. http://glimsworth.example/no
These are the traditional way these types of review sites are organized: dull and boring. I think we can do a lot better than that.
I need a site that will capture attention end engage the visitor; a site that will create a more interactive and less passive user experience.
Scope of work should also include logo font and additional content space for articles, FAQ, widgets, social media links, etc.

Not sure what to advise you as best format - maybe a flash or js carousel, gallery, wheel, logo image matrix, or something else.
Maybe some kind of interactive logo matrix such as this site: http://www.quarnibo.example/
Please apply your best creative mind work to this problem.
Also, please think about creative use of background images, stock photos, etc.
For logo font use can use URL “pellrowatt.example” as placeholder.

```html
<!DOCTYPE html>
<html lang="en">
<head>
<meta charset="utf-8">
<title>Velorim – Consumer Lending</title>
<link rel="stylesheet" href="https://fonts.googleapis.com/css2?family=Abel&family=Arimo:wght@400;700&family=Oswald:wght@500&display=swap">
<style>
:root{
  --sky:#dcedf7;
  --navy:#0f3d63;
  --blue:#1d6ea8;
  --blue-dark:#155b8e;
  --panel:#e3f2fb;
  --panel-line:#b9d9ec;
  --ink:#333;
  --muted:#555;
  --star:#5a9fd4;
  --orange:#f5a623;
  --orange-dark:#d9831a;
  --footer:#0d2437;
}
*{box-sizing:border-box;margin:0;padding:0}
html,body{width:870px;height:1200px;overflow:hidden}
body{position:relative;background:#fff;font-family:"Arimo",Arial,sans-serif;color:var(--ink);font-size:7.4px}
.header{position:absolute;left:0;top:0;width:870px;height:118px;background:linear-gradient(#eaf5fb,var(--sky) 70%)}
.brand{position:absolute;left:129px;top:16px;font-family:"Oswald",sans-serif;font-size:27px;letter-spacing:1px;color:#3a2e26}
.flags{position:absolute;left:130px;top:62px;display:flex;gap:12px}
.flag{width:14px;height:9px;border:1px solid #ccc}
.flag.a{background:#1a2f8a}
.flag.b{background:linear-gradient(#d62b2b 33%,#fff 33% 66%,#d62b2b 66%)}
.flag.c{background:linear-gradient(#2a9fd6 33%,#d62b2b 33% 66%,#3aa84a 66%)}
.header-art{position:absolute;left:450px;top:14px;width:335px;height:68px;background:linear-gradient(rgba(63,134,189,0),rgba(45,115,169,.55))}
.search{position:absolute;left:639px;top:13px;width:96px;height:16px;background:#fff;border:1px solid #c6d6e0;font-size:7px;color:#999;padding:3px 5px}
.nav{position:absolute;left:0;top:82px;width:870px;height:36px;background:linear-gradient(var(--blue),var(--blue-dark));border-top:2px solid #3d8fc7}
.nav ul{list-style:none;display:flex;position:absolute;left:129px;top:0;height:34px}
.nav li{font-family:"Abel",sans-serif;font-size:11px;color:#fff;padding:0 15px;line-height:34px;border-right:1px solid #3b85ba}
.nav li:first-child{padding-left:12px}
.hero{position:absolute;left:129px;top:126px;width:612px;height:165px;border:1px solid #ddd;background:#fff}
.hero h1{position:absolute;left:16px;top:20px;font-family:"Abel",sans-serif;font-weight:400;font-size:22px;line-height:27px;color:var(--blue)}
.hero p{position:absolute;left:16px;top:78px;width:232px;font-size:7.2px;line-height:12px;color:#333}
.dots{position:absolute;left:17px;top:141px;display:flex;gap:1px}
.dots span{width:9px;height:9px;border-radius:50%;background:#777}
.dots span:first-child{background:var(--blue)}
.hero-photo{position:absolute;right:0;top:0;width:305px;height:163px;background:linear-gradient(135deg,#f4f4f4,#cfcfcf 55%,#555)}
.side{position:absolute;left:129px;width:155px}
.panel-head{height:28px;background:linear-gradient(var(--blue),var(--blue-dark));color:#fff;font-family:"Abel",sans-serif;font-size:11px;line-height:28px;padding-left:14px}
.panel-body{background:var(--panel);border-bottom:2px solid var(--blue-dark);padding:10px 18px}
.panel-body li{list-style:none;font-size:7.2px;color:var(--muted);line-height:14.7px}
.panel-body li.lead{color:#222}
.panel-body li.sub::before{content:"» ";color:#222}
.field-label{font-size:7.2px;line-height:9px;color:var(--muted);margin-bottom:3px}
.field-label.tight{margin-bottom:6px}
.field{width:68px;height:18px;background:#fff;border:1px solid #d4e6f1;font-size:7.2px;padding:4px 7px;margin-bottom:9px;color:#222}
.radio{display:flex;align-items:center;gap:5px;font-size:7.2px;color:#222;margin-top:6px}
.radio i{width:7px;height:7px;border:1px solid #888;border-radius:50%;background:#fff}
.vote-btn{display:inline-block;margin-top:6px;background:var(--orange);border:1px solid var(--orange-dark);color:#fff;font-size:7px;padding:3px 7px}
.main{position:absolute;left:290px;top:298px;width:451px}
.main h2{font-family:"Abel",sans-serif;font-weight:400;font-size:11px;color:#222}
.table{position:absolute;left:0;top:27px;width:451px;border:1px solid var(--panel-line);border-top:none}
.thead{height:27px;background:linear-gradient(var(--blue),var(--blue-dark));display:grid;grid-template-columns:88px 67px 67px 108px 53px 1fr;color:#fff;font-family:"Abel",sans-serif;font-size:8.5px;line-height:27px;text-align:center}
.row{height:64.3px;display:grid;grid-template-columns:88px 1fr;border-top:1px solid var(--panel-line);background:var(--panel)}
.supplier{border-right:1px solid var(--panel-line);display:flex;flex-direction:column;align-items:center;padding-top:6px}
.mark{width:70px;height:33px;background:#fff;display:flex;align-items:center;justify-content:center;font-weight:700;font-size:10px;color:var(--navy)}
.supplier-name{font-size:7.2px;color:#222;margin-top:9px}
.cells{display:grid;grid-template-columns:67px 67px 108px 53px 1fr;grid-template-rows:49px 1fr}
.cell{font-size:6.9px;line-height:9px;color:#222;padding-top:12px;text-align:center}
.cell.type{text-align:left;padding-left:6px}
.cell.req{padding-left:2px;padding-right:2px}
.stars{display:flex;gap:1px;margin-top:6px}
.stars svg{width:8px;height:8px;fill:var(--star)}
.cell.apply{border-left:1px solid var(--panel-line)}
.apply-btn{display:inline-block;background:linear-gradient(#fbb94c,var(--orange));border:1px solid var(--orange-dark);color:#fff;font-size:6.8px;padding:2px 4px;margin-top:-2px}
.note{grid-column:1/-1;border-top:1px solid var(--panel-line);font-size:6.9px;color:#222;padding:4px 7px}
.article{position:absolute;left:292px;top:876px;width:449px;border-top:2px solid var(--blue-dark);padding-top:10px}
.article h3{font-family:"Abel",sans-serif;font-weight:400;font-size:11px;color:#222;margin-bottom:11px}
.article p{font-size:6.9px;line-height:11px;color:#333;text-align:justify;margin-bottom:11px}
.footer{position:absolute;left:0;top:1150px;width:870px;height:50px;background:var(--footer)}
.footer-links{position:absolute;left:134px;top:12px;font-size:7px;color:#a8bdcc}
.copyright{position:absolute;left:134px;top:29px;font-size:7px;color:#a8bdcc}
.social{position:absolute;left:635px;top:15px;display:flex;gap:10px;align-items:center}
.social span{width:19px;height:19px;border-radius:2px}
.social .s1{background:#3eb4e6}.social .s2{background:#3b5a9a}.social .s3{background:#333}.social .s4{background:#f47b20}
.social em{font-style:normal;font-size:7px;color:#8da2b2;margin-left:2px}
</style>
</head>
<body>
<svg width="0" height="0" style="position:absolute"><defs><symbol id="star" viewBox="0 0 10 10"><path d="M5 0l1.5 3.3 3.5.3-2.7 2.3.9 3.5L5 7.6 1.8 9.4l.9-3.5L0 3.6l3.5-.3z"/></symbol></defs></svg>

<header class="header">
  <div class="brand">VELORIM</div>
  <div class="flags"><span class="flag a"></span><span class="flag b"></span><span class="flag c"></span></div>
  <div class="header-art" role="img" aria-label="City skyline illustration"></div>
  <div class="search">Search</div>
  <nav class="nav"><ul>
    <li>HOME</li><li>ALL ABOUT FINANCES</li><li>FINANCE DICTIONARY</li><li>ABOUT US</li><li>PLUG</li><li>FORUM</li>
  </ul></nav>
</header>

<section class="hero">
  <h1>WE CAN BE YOUR GUIDE<br>IN THE WORLD OF FINANCE!</h1>
  <p>Morbi nunc odio cursus nec luctus a lorem. Maecenas tristique orci ac sem. Duis ultricies pharetra magna. Donec accumsan malesuada orci. Donec sit amet eros. Lorem ipsum dolor sit amet.</p>
  <div class="dots"><span></span><span></span><span></span><span></span></div>
  <div class="hero-photo" role="img" aria-label="Photo of a calculator lying on financial paperwork"></div>
</section>

<aside class="side" style="top:298px">
  <div class="panel-head">CHOOSE YOUR LOAN HERE</div>
  <ul class="panel-body" style="height:108px">
    <li class="lead">ALL LOANS</li><li class="sub">Favoritlån</li><li class="sub">Consumer Lending</li><li class="sub">Car Loans</li><li class="sub">Unsecured Loans</li><li class="sub">Consumer loans</li>
  </ul>
</aside>
<aside class="side" style="top:440px">
  <div class="panel-head">CALCULATE A LOAN</div>
  <div class="panel-body" style="height:181px">
    <div class="field-label">Loan Amount</div><div class="field">25,000</div>
    <div class="field-label">Effective interest rate</div><div class="field">15</div>
    <div class="field-label">Maturity</div><div class="field">10</div>
    <div class="field-label tight">Monthly cost</div><div class="field-label">GBP</div><div class="field">403.34</div>
  </div>
</aside>
<aside class="side" style="top:655px">
  <div class="panel-head">INFORMATION</div>
  <ul class="panel-body" style="height:42px;padding-top:6px">
    <li class="sub">User Panel</li><li class="sub">Calculate a loan</li>
  </ul>
</aside>
<aside class="side" style="top:730px">
  <div class="panel-head">VOTE</div>
  <div class="panel-body" style="height:89px;padding-top:8px">
    <div class="field-label">Did you do a private budget:</div>
    <div class="radio"><i></i>Yes</div>
    <div class="radio"><i></i>No</div>
    <div class="radio"><i></i>Do not know</div>
    <span class="vote-btn">VOTE</span>
  </div>
</aside>

<main class="main">
  <h2>CONSUMER LENDING</h2>
  <div class="table">
    <div class="thead"><span>SUPPLIER</span><span>TYPE</span><span>AMOUNT</span><span>REQUIREMENTS</span><span>SEE MORE</span><span></span></div>

    <div class="row"><div class="supplier"><div class="mark">KORVANT</div><div class="supplier-name">KORVANT</div></div>
      <div class="cells"><div class="cell type">Consumer loans<div class="stars"><svg><use href="#star"/></svg><svg><use href="#star"/></svg><svg><use href="#star"/></svg><svg><use href="#star"/></svg><svg><use href="#star"/></svg></div></div><div class="cell">10,000 to 100,000</div><div class="cell req">Age of 20. No betalningsanm. Annual income less than 120,000 €.</div><div class="cell">Read more</div><div class="cell apply"><span class="apply-btn">APPLY HERE</span></div><div class="note">Save time and money by signing your loan agreement electronically!</div></div></div>

    <div class="row"><div class="supplier"><div class="mark">TRELMIKA</div><div class="supplier-name">TRELMIKA</div></div>
      <div class="cells"><div class="cell type">Consumer loans<div class="stars"><svg><use href="#star"/></svg><svg><use href="#star"/></svg><svg><use href="#star"/></svg><svg><use href="#star"/></svg><svg><use href="#star"/></svg></div></div><div class="cell">10,000 to 100,000</div><div class="cell req">Age of 20. No betalningsanm. Annual income less than 120,000 €.</div><div class="cell">Read more</div><div class="cell apply"><span class="apply-btn">APPLY HERE</span></div><div class="note">Save time and money by signing your loan agreement electronically!</div></div></div>

    <div class="row"><div class="supplier"><div class="mark">Odenvik Bank</div><div class="supplier-name">ODENVIK BANK</div></div>
      <div class="cells"><div class="cell type">Consumer loans<div class="stars"><svg><use href="#star"/></svg><svg><use href="#star"/></svg><svg><use href="#star"/></svg><svg><use href="#star"/></svg><svg><use href="#star"/></svg></div></div><div class="cell">10,000 to 100,000</div><div class="cell req">Age of 20. No betalningsanm. Annual income less than 120,000 €.</div><div class="cell">Read more</div><div class="cell apply"><span class="apply-btn">APPLY HERE</span></div><div class="note">Save time and money by signing your loan agreement electronically!</div></div></div>

    <div class="row"><div class="supplier"><div class="mark">BRAXEL</div><div class="supplier-name">BRAXEL</div></div>
      <div class="cells"><div class="cell type">Consumer loans<div class="stars"><svg><use href="#star"/></svg><svg><use href="#star"/></svg><svg><use href="#star"/></svg><svg><use href="#star"/></svg><svg><use href="#star"/></svg></div></div><div class="cell">10,000 to 100,000</div><div class="cell req">Age of 20. No betalningsanm. Annual income less than 120,000 €.</div><div class="cell">Read more</div><div class="cell apply"><span class="apply-btn">APPLY HERE</span></div><div class="note">Save time and money by signing your loan agreement electronically!</div></div></div>

    <div class="row"><div class="supplier"><div class="mark">PENNISO</div><div class="supplier-name">PENNISO</div></div>
      <div class="cells"><div class="cell type">Consumer loans<div class="stars"><svg><use href="#star"/></svg><svg><use href="#star"/></svg><svg><use href="#star"/></svg><svg><use href="#star"/></svg><svg><use href="#star"/></svg></div></div><div class="cell">10,000 to 100,000</div><div class="cell req">Age of 20. No betalningsanm. Annual income less than 120,000 €.</div><div class="cell">Read more</div><div class="cell apply"><span class="apply-btn">APPLY HERE</span></div><div class="note">Save time and money by signing your loan agreement electronically!</div></div></div>

    <div class="row"><div class="supplier"><div class="mark">MIRLA</div><div class="supplier-name">MIRLA</div></div>
      <div class="cells"><div class="cell type">Consumer loans<div class="stars"><svg><use href="#star"/></svg><svg><use href="#star"/></svg><svg><use href="#star"/></svg><svg><use href="#star"/></svg><svg><use href="#star"/></svg></div></div><div class="cell">10,000 to 100,000</div><div class="cell req">Age of 20. No betalningsanm. Annual income less than 120,000 €.</div><div class="cell">Read more</div><div class="cell apply"><span class="apply-btn">APPLY HERE</span></div><div class="note">Save time and money by signing your loan agreement electronically!</div></div></div>

    <div class="row"><div class="supplier"><div class="mark">SKOVARD</div><div class="supplier-name">SKOVARD</div></div>
      <div class="cells"><div class="cell type">Consumer loans<div class="stars"><svg><use href="#star"/></svg><svg><use href="#star"/></svg><svg><use href="#star"/></svg><svg><use href="#star"/></svg><svg><use href="#star"/></svg></div></div><div class="cell">10,000 to 100,000</div><div class="cell req">Age of 20. No betalningsanm. Annual income less than 120,000 €.</div><div class="cell">Read more</div><div class="cell apply"><span class="apply-btn">APPLY HERE</span></div><div class="note">Save time and money by signing your loan agreement electronically!</div></div></div>

    <div class="row"><div class="supplier"><div class="mark">Altero</div><div class="supplier-name">ALTERO FINANCE</div></div>
      <div class="cells"><div class="cell type">Consumer loans<div class="stars"><svg><use href="#star"/></svg><svg><use href="#star"/></svg><svg><use href="#star"/></svg><svg><use href="#star"/></svg><svg><use href="#star"/></svg></div></div><div class="cell">10,000 to 100,000</div><div class="cell req">Age of 20. No betalningsanm. Annual income less than 120,000 €.</div><div class="cell">Read more</div><div class="cell apply"><span class="apply-btn">APPLY HERE</span></div><div class="note">Save time and money by signing your loan agreement electronically!</div></div></div>
  </div>
</main>

<article class="article">
  <h3>PERSONAL LOANS WITH FLEXIBLE TERMS</h3>
  <p>Sed sagittis, felis at congue laoreet, erat purus sollicitudin ipsum, eu dignissim dui turpis sit amet turpis. Ut at velit sit amet elit volutpat rutrum quis sagittis lectus. Aliquam sed risus vitae erat auctor laoreet ut quis turpis. Donec ut est felis. Proin sit amet magna dolor, et condimentum dui. Cras luctus ipsum augue, ac tincidunt augue. Curabitur ac cursus sem. Mauris lorem nulla, suscipit ut pharetra quis, fringilla aliquam diam. Vivamus sollicitudin, nunc nec egestas semper, sem ante laoreet nisi, suscipit porta nulla velit ut sem. Praesent eget sem in lorem vehicula consequat quis vel sapien. In quis enim vitae ante ultricies eleifend eget vitae velit.</p>
  <p>Donec sed sem sed sem suscipit tempor placerat a velit. Mauris luctus tincidunt magna, sed congue dolor luctus in. Praesent condimentum, ante sit amet vestibulum lobortis, massa sem interdum dui, ac fermentum erat leo non purus. Phasellus elementum velit quis mauris consectetur id pharetra tortor consectetur. Sed vel convallis lorem. Sed tempus, diam eget rhoncus faucibus, velit ante vestibulum ipsum, a mollis odio neque vel turpis. Etiam scelerisque malesuada augue, a mattis elit mollis in. Phasellus id urna ac nibh malesuada adipiscing vitae a ligula. Pellentesque vehicula, ipsum vel faucibus varius, massa ligula vulputate eros, eu mollis nunc purus sit amet turpis. Mauris eu ipsum erat. Mauris rhoncus, ante a malesuada egestas, urna nisl consequat ante, quis pellentesque ante nibh nec lorem. Donec id venenatis elit. Donec lacinia, sem tincidunt semper suscipit, lacus dolor fermentum dui, vitae suscipit orci turpis quis felis. Nam felis mi, sodales id tincidunt ac, faucibus ut libero. Etiam blandit tempor dictum.</p>
  <p>Vivamus justo sem, auctor non scelerisque eu, pretium a lorem. Nam aliquam commodo risus ac interdum. Donec facilisis nisl sit amet mi tempor blandit. Pellentesque at risus eros, convallis mollis diam. Class aptent taciti sociosqu ad litora torquent per conubia nostra, per inceptos himenaeos. Sed lectus augue, venenatis id egestas sed, semper vitae neque. Integer nec tortor non metus porta iaculis non ultrices mauris. Aliquam sed feugiat nisi. Sed turpis nisl, porttitor quis tincidunt et, pharetra id odio. Cum sociis natoque penatibus et magnis dis parturient montes, nascetur ridiculus mus. Vivamus eget magna vitae arcu fermentum faucibus id ac ligula.</p>
</article>

<footer class="footer">
  <div class="footer-links">Home | All about finances | Finance Dictionary | About Us | Plug | Forum</div>
  <div class="copyright">Copyright © Velorim 2012 - All Rights Reserved</div>
  <div class="social"><span class="s1"></span><span class="s2"></span><span class="s3"></span><span class="s4"></span><em>M3</em></div>
</footer>
</body>
</html>
```